Project: Stationary for product web site
Stationary for product web site - Automotive
Bright & Fun-filled
Dorian Feltz
Directory of Marketing
7213 W. Pellam Avenue # 208 Lauderhill, FL, 33329
dorian.feltz@quillmarkgear.com
Xpert Xpert

```html
<!DOCTYPE html>
<html lang="en">
<head>
<meta charset="utf-8">
<title>Quillmark Gear – Business Cards</title>
<link href="https://fonts.googleapis.com/css2?family=Rubik:wght@400;500;700&display=swap" rel="stylesheet">
<style>
  :root{
    --bg:#e9e9eb;
    --card:#ffffff;
    --blue:#2b3f9f;
    --blue-deep:#1c2a78;
    --blue-light:#6f82d8;
    --orange:#f26a1b;
    --ink:#3a3a3a;
    --muted:#6b6b6b;
  }
  *{box-sizing:border-box;margin:0;padding:0}
  html,body{width:1200px;height:883px;overflow:hidden}
  body{background:var(--bg);font-family:"Rubik",Arial,sans-serif;position:relative}
  .card{
    position:absolute;width:540px;height:310px;background:var(--card);
    border-radius:22px;box-shadow:0 6px 18px rgba(0,0,0,.12);overflow:hidden;
  }
  .card--front{left:40px;top:300px}
  .card--back{left:620px;top:300px}
  .wordmark{
    position:absolute;left:0;right:0;text-align:center;
    color:var(--blue);font-weight:700;font-size:34px;letter-spacing:.5px;
  }
  .card--front .wordmark{top:52px;font-size:30px}
  .card--back .wordmark{top:128px}
  .person{position:absolute;left:30px;top:112px;border-left:3px solid var(--orange);padding-left:8px}
  .person__name{font-size:12px;font-weight:500;color:var(--ink);text-transform:uppercase;letter-spacing:.5px}
  .person__title{font-size:10px;color:var(--muted);margin-top:2px}
  .contacts{position:absolute;left:30px;top:160px;list-style:none}
  .contacts li{display:flex;align-items:center;font-size:9.5px;color:var(--ink);height:15px}
  .contacts svg{width:9px;height:9px;margin-right:7px;fill:var(--orange)}
  .address{position:absolute;left:372px;top:160px;width:150px;font-size:9.5px;line-height:1.45;color:var(--ink)}
  .band{position:absolute;left:0;bottom:48px;width:540px;height:30px}
</style>
</head>
<body>
  <section class="card card--front">
    <div class="wordmark">Quillmark Gear</div>
    <div class="person">
      <p class="person__name">Dorian Feltz</p>
      <p class="person__title">Managing Director</p>
    </div>
    <ul class="contacts">
      <li><svg viewBox="0 0 10 10"><path d="M2 0h2l1 3-1.5 1a6 6 0 0 0 2.5 2.5L7 5l3 1v2a2 2 0 0 1-2 2A8 8 0 0 1 0 2a2 2 0 0 1 2-2z"/></svg>012 555 0147</li>
      <li><svg viewBox="0 0 10 10"><path d="M2 0h2l1 3-1.5 1a6 6 0 0 0 2.5 2.5L7 5l3 1v2a2 2 0 0 1-2 2A8 8 0 0 1 0 2a2 2 0 0 1 2-2z"/></svg>012 555 0193</li>
      <li><svg viewBox="0 0 10 10"><path d="M2 0h2l1 3-1.5 1a6 6 0 0 0 2.5 2.5L7 5l3 1v2a2 2 0 0 1-2 2A8 8 0 0 1 0 2a2 2 0 0 1 2-2z"/></svg>012 555 0168</li>
      <li><svg viewBox="0 0 10 10"><rect x="0" y="2" width="10" height="6" rx="1"/></svg>dorian.feltz@quillmarkgear.com</li>
      <li><svg viewBox="0 0 10 10"><circle cx="5" cy="5" r="5"/></svg>www.quillmarkgear.com</li>
    </ul>
    <p class="address">7213 W. Pellam Avenue # 208<br>Lauderhill, FL, 33329</p>
    <svg class="band" viewBox="0 0 540 30" preserveAspectRatio="none" aria-hidden="true">
      <defs>
        <linearGradient id="bandFill" x1="0" x2="1" y1="0" y2="0">
          <stop offset="0" stop-color="#ffffff" stop-opacity="0"/>
          <stop offset=".25" stop-color="var(--blue-light)"/>
          <stop offset=".5" stop-color="var(--blue)"/>
          <stop offset="1" stop-color="var(--blue-deep)"/>
        </linearGradient>
      </defs>
      <path d="M0 22 Q200 4 540 0 V30 H0 Z" fill="url(#bandFill)"/>
    </svg>
  </section>

  <section class="card card--back">
    <div class="wordmark">Quillmark Gear</div>
  </section>
</body>
</html>
```